Business Card/Design Project for Personal Injury Lawyer

Personal Injury Attorney. I represent people who have been injured in accidents and are making money damage claims against the negligent party. As a personal injury attorney, I am a counselor, advisor, and legal representative to my clients. Clients want someone who is aggresssive yet professional.

More information about what I do an be found at www.dravolinlaw.com

Target Market(s)

General public.

Industry/Entity Type

Legal

Contact Information for Business Card

Need a new logo/brand image for b-cards, website, and letterhead/envelops. Looking for something original (no scales of justice or courthouse columns), yet classy and professional.

Here's what I'm thinking (but I'm always open to other ideas):

On the front, I would like my name (Corwin T. Dravolin), and underneath the words "Personal Injury Attorney." The background could be black, for example, and the lettering could be white or foil. I'm open to differnt colors, or even two colors. My name on the front side should pop.

And then on the back would be all my contact info, and maybe a logo or a slogan.

Here are two slogans I've come up with so far: 1. Settle for More. 2. Serious Results for the Seriously Injured.

Requirements
Must have
• Something that identifys me as a personal injury attorney, such as the words Personal Injury Attorney (or Lawyer, or Law Firm, etc.).
Nice to have
• A style/image that can be used nicely on my website and on letterhead.
Should not have
• Tired, commonly used logos or symbols, such a scales of justice or courthouse columns.

```html
<!DOCTYPE html>
<html lang="en">
<head>
<meta charset="utf-8">
<title>Dravolin Law – Business Card</title>
<link rel="stylesheet" href="https://fonts.googleapis.com/css2?family=Cinzel:wght@400&family=Open+Sans:wght@400;600&display=swap">
<style>
  :root {
    --red: #ec0016;
    --charcoal: #2e2f31;
    --white: #ffffff;
    --rule: #9a9a9a;
    --canvas: #e9e6e3;
  }
  * { margin: 0; padding: 0; box-sizing: border-box; }
  html, body { width: 1200px; height: 900px; overflow: hidden; }
  body { background: var(--canvas); position: relative; font-family: "Open Sans", Arial, sans-serif; }

  .card { position: absolute; overflow: hidden; box-shadow: 0 6px 18px rgba(0,0,0,.18); }

  .card-front { left: 77px; top: 33px; width: 589px; height: 364px; background: var(--white); }
  .card-front .bands { position: absolute; inset: 0; }

  .brand-front {
    position: absolute; left: 118px; top: 88px; width: 390px;
    display: flex; align-items: center; justify-content: center; gap: 16px;
  }
  .brand-mark { width: 22px; height: 22px; border: 2px solid var(--red); }
  .brand-name {
    font-family: "Cinzel", Georgia, serif; font-weight: 400;
    font-size: 38px; letter-spacing: 1px; color: var(--red); white-space: nowrap;
  }

  .contact-list {
    position: absolute; right: 316px; top: 250px; list-style: none;
    color: var(--white); font-size: 15px; line-height: 24.5px; text-align: right;
  }
  .contact-list li { display: flex; justify-content: flex-end; align-items: center; gap: 9px; }
  .contact-list svg { width: 12px; height: 12px; fill: var(--white); flex: none; }

  .attorney { position: absolute; left: 313px; top: 273px; color: var(--white); }
  .attorney-name { font-weight: 600; font-size: 20px; line-height: 28px; }
  .attorney-title { font-size: 15px; line-height: 22px; }

  .card-back { left: 388px; top: 505px; width: 566px; height: 352px; background: var(--red); }
  .brand-back {
    position: absolute; left: 0; right: 0; top: 140px; text-align: center;
    font-family: "Cinzel", Georgia, serif; font-weight: 400;
    font-size: 42px; letter-spacing: 1px; color: var(--white); white-space: nowrap;
  }
</style>
</head>
<body>

<section class="card card-front" aria-label="Business card front">
  <svg class="bands" viewBox="0 0 589 364" width="589" height="364" aria-hidden="true">
    <polygon points="0,200 406,200 384,225 0,225" fill="var(--charcoal)"/>
    <polygon points="415,192 589,192 589,364 0,364 0,230 386,230" fill="var(--red)"/>
  </svg>

  <div class="brand-front">
    <span class="brand-mark" aria-hidden="true"></span>
    <span class="brand-name">Dravolin Law</span>
  </div>

  <ul class="contact-list">
    <li>(044)-555-0190
      <svg viewBox="0 0 24 24"><path d="M6.6 10.8a15 15 0 0 0 6.6 6.6l2.2-2.2c.3-.3.7-.4 1-.2 1.1.4 2.3.6 3.6.6.6 0 1 .4 1 1V20c0 .6-.4 1-1 1A17 17 0 0 1 3 4c0-.6.4-1 1-1h3.5c.6 0 1 .4 1 1 0 1.3.2 2.5.6 3.6.1.3 0 .7-.2 1z"/></svg></li>
    <li>555-010-7890
      <svg viewBox="0 0 24 24"><path d="M6 2h9v5h3a2 2 0 0 1 2 2v11a2 2 0 0 1-2 2H6a2 2 0 0 1-2-2V4a2 2 0 0 1 2-2zm2 10v2h3v-2zm5 0v2h3v-2zm-5 4v2h3v-2zm5 0v2h3v-2zM8 4v4h5V4z"/></svg></li>
    <li>info@dravolinlaw.com
      <svg viewBox="0 0 24 24"><path d="M2 5h20v14H2zm2 2v.5l8 5 8-5V7l-8 5z"/></svg></li>
    <li>www.dravolinlaw.com
      <svg viewBox="0 0 24 24"><circle cx="12" cy="12" r="10"/></svg></li>
  </ul>

  <div class="attorney">
    <p class="attorney-name">Corwin T. Dravolin</p>
    <p class="attorney-title">Personal Injury Attorney</p>
  </div>
</section>

<section class="card card-back" aria-label="Business card back">
  <p class="brand-back">Dravolin Law</p>
</section>

</body>
</html>
```